BrindleYards.com website homepage re-design

Introduction

Over the last few months, we have dealt with what we would consider B-level website designers. Either they are not up to date with current design techniques, are lazy, or don’t speak English well enough to complete the job. We like to think that we are patient, but this time we are looking (and paying for) top notch service.

Here is a link to the last project that is failing - not because it doesn't have potential, but because the design team really just can't get it together. (also, the front page is just too busy)

http://www.kavelworks.com/project/brindleyards/

We want a new website that lives up to our name as the best professional poker staking company (to understand what we do, look at the current website) in the world and catches the eye of any potential customers/clients.

We need a bright mind that is going to be creative and help us build a powerful website that will stand out among our competitors. We want to be hands-on and give feedback as often as we can.

*****We understand that this project is only for the front page of the site******

What We Do Not Want

Below are website designers that have NOT lived up to our expectations. Please review their portfolios. If you are similar to them in skill, please do not bid. Sorry if this sounds harsh.

http://www.tarn-studio.com/
www.quelvant.com
http://www.pixelmoor.com/

**The graphic images and logo were designed by a third party. We think they are good, although might not really “fit” on the website as is shown now.

I uploaded a Zip file with all the source files here: http://www.filequarry.com/?d=9T2KWMPL

A few good websites we like

http://www.thegrove.com.au/
http://www.halvinger.com.au/

Front Page

Current: http://brindleyards.com/

What we want is a clear, strong, direct message displayed through an animated Flash introduction which really gets our ethos across (see examples below);

We provide staking, free coaching, housing, top notch support and makeup free reward trips to live events which is a massive selling point to those players who are taking poker seriously, so much so that it could and should, along with the amazing coaching we provide, entice players to join even if they don't really need staking. No other site provides this as far as we know and should be a big part of the attraction to our site.

Obviously, the exact details of what we do will need to be explained via AIM or the phone.

We are the best at what we do and we need to convey that in an impressive way. We offer free coaching, amazing free trips, a forum, a great team environment.

Right now, we have too much going on with the front page, and it needs to be turned into secondary pages

A few websites we like that have strong front page messages are.

***We also have a logo design contest up.
Updates

Industry/Entity Type

Events

Requirements
Must have
• Flash

```html
<!DOCTYPE html>
<html lang="en">
<head>
<meta charset="utf-8">
<title>Brindle Yards — Online Poker Staking</title>
<link href="https://fonts.googleapis.com/css2?family=Montserrat:wght@400;600;700&family=Open+Sans:wght@400;600;700&display=swap" rel="stylesheet">
<style>
:root{
  --bg:#1c1c1c;
  --panel-line:#3a3a3a;
  --text:#e8e8e8;
  --muted:#b4b4b4;
  --accent:#2ec4f2;
  --blue:#1e8fe0;
  --green:#a6e22e;
  --white:#ffffff;
}
*{box-sizing:border-box;margin:0;padding:0}
html,body{width:1200px;height:1200px;overflow:hidden}
body{background:radial-gradient(ellipse at 50% 0%,#262626 0%,var(--bg) 55%,#171717 100%);color:var(--text);font-family:"Open Sans",sans-serif;position:relative}
.search{position:absolute;left:908px;top:0;width:174px;height:35px;background:#5bb8e8;border-radius:0 0 6px 6px;padding:8px 10px}
.search-field{background:#fff;height:19px;border:1px solid #3d8fc0;font-size:9px;color:#999;padding:3px 6px;display:flex;justify-content:space-between;align-items:center}
.brand{position:absolute;left:0;right:0;top:38px;display:flex;justify-content:center;align-items:center;gap:14px}
.brand-dot{width:40px;height:40px;border-radius:50%;background:var(--blue)}
.brand-name{font-family:"Montserrat",sans-serif;font-weight:700;font-size:36px;letter-spacing:2px;color:var(--white)}
.nav{position:absolute;left:120px;top:132px;display:flex}
.nav-item{width:120px;height:36px;border-left:1px solid #444;padding:5px 9px;font-family:"Montserrat",sans-serif;font-size:10px;letter-spacing:1px;color:#ddd;line-height:12px;text-transform:uppercase}
.nav-item.is-active{background:#3a3a3a}
.nav-rule{position:absolute;left:0;top:168px;width:1200px;height:6px;background:var(--white)}
.hero{position:absolute;left:132px;top:194px;width:940px;height:346px;border-radius:8px;overflow:hidden;background:radial-gradient(ellipse at 78% 40%,#4fc3ff 0%,#1273c9 28%,#062a55 55%,#03070d 80%)}
.hero-text{position:absolute;left:56px;top:130px}
.hero-name{font-family:"Montserrat",sans-serif;font-weight:700;font-size:30px;letter-spacing:4px;color:var(--white)}
.hero-line{font-family:"Montserrat",sans-serif;font-weight:700;font-size:38px;color:var(--accent);margin-top:8px}
.hero-line .lead{font-size:19px;color:var(--green);margin-right:6px}
.divider{position:absolute;left:160px;width:880px;height:1px;background:linear-gradient(90deg,transparent,#555 20%,#555 80%,transparent)}
.welcome{position:absolute;left:0;right:0;top:576px;text-align:center}
.welcome h1{font-family:"Montserrat",sans-serif;font-weight:700;font-size:28px;letter-spacing:.3px;color:var(--white);line-height:34px}
.welcome p{width:820px;margin:6px auto 0;font-family:"Montserrat",sans-serif;font-size:17.5px;line-height:20px;color:var(--text)}
.more{color:var(--accent);font-weight:600}
.features{position:absolute;left:130px;top:720px;display:flex;gap:20px}
.feature{width:220px}
.feature h2{font-family:"Montserrat",sans-serif;font-weight:700;font-size:13.5px;letter-spacing:-.1px;white-space:nowrap;color:var(--white);height:27px;line-height:18px}
.feature-media{width:220px;height:100px;border:3px solid #cfcfcf}
.feature p{margin-top:11px;font-size:9.4px;line-height:14px;color:var(--muted);letter-spacing:.3px}
.feature .link{color:var(--accent);white-space:nowrap}
.updates{position:absolute;left:120px;top:1076px;width:960px;height:85px;border-top:1px solid var(--panel-line);border-bottom:1px solid var(--panel-line);display:flex}
.update{padding:12px 10px 0;font-size:9.6px;color:var(--muted)}
.update:nth-child(1){width:310px}
.update:nth-child(2){width:320px}
.update:nth-child(3){width:330px}
.update + .update{border-left:1px solid var(--panel-line);margin:12px 0;padding-top:0;padding-left:18px}
.update h3{font-family:"Montserrat",sans-serif;font-size:11px;font-weight:700;color:var(--white)}
.update h3 span{color:var(--accent);font-size:9px;font-weight:400;margin-left:8px}
.update-title{font-weight:700;font-size:11px;color:var(--white);margin-top:3px}
.blog{display:flex;gap:8px;margin-top:4px}
.avatar{width:34px;height:34px;background:linear-gradient(#6b5a4a,#2f2a26)}
.blog-title{color:var(--accent);font-weight:700;font-size:12px}
.quote-by{text-align:right;font-style:italic;margin-top:3px}
.copyright{position:absolute;right:130px;top:1172px;font-size:9px;color:#777}
</style>
</head>
<body>
<div class="search"><div class="search-field">search...<svg width="9" height="9" viewBox="0 0 10 10"><circle cx="4" cy="4" r="3" fill="none" stroke="#aaa" stroke-width="1.4"/><line x1="6.3" y1="6.3" x2="9" y2="9" stroke="#aaa" stroke-width="1.4"/></svg></div></div>

<header class="brand"><span class="brand-dot"></span><span class="brand-name">BRINDLE YARDS</span></header>

<nav class="nav">
  <div class="nav-item is-active">Home</div>
  <div class="nav-item">Management<br>Team</div>
  <div class="nav-item">Coaching</div>
  <div class="nav-item">FAQs</div>
  <div class="nav-item">Contact Us</div>
  <div class="nav-item">Forums</div>
  <div class="nav-item">Poker<br>Radio</div>
  <div class="nav-item">Apply</div>
</nav>
<div class="nav-rule"></div>

<section class="hero" role="img" aria-label="Banner illustration of glowing blue poker chips around a stacked-chip barn">
  <div class="hero-text">
    <div class="hero-name">BRINDLE YARDS</div>
    <div class="hero-line"><span class="lead">ONLINE</span>POKER STAKING</div>
  </div>
</section>

<div class="divider" style="top:558px"></div>
<section class="welcome">
  <h1>WELCOME TO BRINDLE YARDS</h1>
  <p>Our mission is to invest in the best online poker players, build a professional and personal relationship with them, and profit together as a team. We stake players in low-stakes cash games to high-stakes multi-table tournaments and everything in between. &nbsp;| &nbsp;<span class="more">READ MORE</span></p>
</section>
<div class="divider" style="top:700px"></div>

<section class="features">
  <article class="feature">
    <h2>STAKING</h2>
    <div class="feature-media" role="img" aria-label="Online poker staking graphic with blue chips" style="background:linear-gradient(90deg,#fff 45%,#bfe3fb 70%,#3a9be8)"></div>
    <p>Staking is the core of our business. We began BrindleYards with the goal of being the most-player friendly backers in the world, and we continue to strive to meet those lofty expectations. Our team of players consists of low stakes players, high stakes players, and everyone in between. We back all limits and all games both live and online. All Brindle players, not only the high-stakes players, enjoy great benefits, such as free live, all-expense paid poker trips around the world, reduced rate housing in Las Vegas and Atlantic City, free coaching, and many other perks. <span class="link"><span style="color:var(--muted)">&nbsp;|&nbsp;</span> READ MORE</span></p>
  </article>
  <article class="feature">
    <h2>STRATEGY</h2>
    <div class="feature-media" role="img" aria-label="Fanned playing cards on white" style="background:linear-gradient(135deg,#f4f4f4,#dcdcdc)"></div>
    <p>The newly launched Brindle Strateg offers a great opportunity to improve your poker game. Watch videos and listen to commentary from some of the best poker players in the world. Videos and commentary include HU Sngs, Cash games, 180-man turbos, mtts and more. We hope that Brindle Strategy becomes a regular part of your poker successes. As a special introductory offer, all content will be free! <span class="link"><span style="color:var(--muted)">&nbsp;|&nbsp;</span> READ MORE</span></p>
  </article>
  <article class="feature">
    <h2>FORUMS</h2>
    <div class="feature-media" role="img" aria-label="Forum page screenshot with blue chips" style="background:linear-gradient(135deg,#2d7fd0,#dce9f5 45%,#f2f6fa 60%,#3a8fe0)"></div>
    <p>The Brindle Forums have quickly become the place to discuss poker strategy. The forum is bubbling with poker commentary and questions. Forum members include high-stakes Brindle team members, low-stakes Brindle team members, and many other players simply looking to improve their game and communicate with other players. In our opinion, the best way to become a better poker player is to talk poker with other players. The Brindle Forum is the perfect environment. <span class="link"><span style="color:var(--muted)">&nbsp;|&nbsp;</span> READ MORE</span></p>
  </article>
  <article class="feature">
    <h2>HAND HISTORY CONVERTER</h2>
    <div class="feature-media" role="img" aria-label="Blue poker chips on white" style="background:radial-gradient(circle at 20% 40%,#2a8be0 0,#8cc8f5 22%,#fff 40%)"></div>
    <p>Lorem ipsum dolor sit amet, consectetur adipisicing elit, sed do eiusmod tempor incididunt ut labore et dolore magna aliqua. Ut enim ad minim veniam, quis nostrud exercitation ullamco laboris nisi ut aliquip ex ea commodo consequat. Duis aute irure dolor in reprehenderit in voluptate velit esse cillum dolore eu fugiat nulla pariatur. Excepteur sint occaecat cupidatat non proident, sunt in culpa qui officia deserunt mollit anim id est laborum. <span class="link"><span style="color:var(--muted)">&nbsp;|&nbsp;</span> READ MORE</span></p>
  </article>
</section>

<section class="updates">
  <div class="update">
    <h3>RECENT NEWS<span>read more »</span></h3>
    <div class="update-title">Delta Players forums are now OPEN!</div>
    <div>Owens forums are now open to all his students. Be sure to catch the recent Tip Of The Week! // 8 Dec 2010</div>
  </div>
  <div class="update">
    <h3>LATEST BLOG ENTRY<span>read more »</span></h3>
    <div class="blog">
      <div class="avatar" role="img" aria-label="Author photo"></div>
      <div><div class="blog-title">Poker Update!</div><div>tom "riverkid" Hale</div></div>
    </div>
  </div>
  <div class="update">
    <h3>TESTIMONIALS<span>read more »</span></h3>
    <div style="margin-top:3px">"Marty's vast knowledge and laid back coaching style makes every session a great learning experience!..."</div>
    <div class="quote-by">Wade, Arkansas</div>
  </div>
</section>

<footer class="copyright">Copyright (c) 2011, Brindle Yards &nbsp;| &nbsp;All Rights Reserved.</footer>
</body>
</html>
```